VerdaTurf - 11" x 4" Door Hanger, full color both sides

We need a door hanger designed, 11" x 4", full color both sides, We are a lawn care company that provides lawn mowing, and other services to clients. This door hanger will be place on the 9 neighbors of our current clients. The ad needs to state that we provided lawn service to one of their neighbors today, and that we are in their neighborhood each week on that day. The door hanger will have 4 printings, substituting the day of Tuesday, Wednesday, Thursday, and Friday. All the art work and text will remain the same except the day of the week. For information about VerdaTurf, please visit our website www.verdaturf-example.net. The main emphasis of the message should be that we are their every week on that day, and the benefits to them of using our service (ie. quality time with their family, golf, sports, resting, etc., instead of mowing the lawn). At the bottom of the door hanger will be a coupon offering their tenth (10th) lawn service free, which is the same as a 10% discount.

I have uploaded a template files for the front and back of an 11 x 4 door hanger, The templates are pdf, jpeg, or eps files. The final product can be a pdf, jpeg, or eps file.

Target Market(s)

Neighbors of our existing clients

Industry/Entity Type

Lawn Care

Font styles to use
Serif

Requirements
Must have
• Professional design and art, Short conversational message that relays the following thoughts:
• 1. We mowed your neighbor's lawn today!
• 2. We are in your neighborhood every Tuesday!
• 3. Our lawn service is guaranteed.
• 4. Call to action - Call us today! 512-748-3091
• 5. Of course our contact info, name, phone number, website address.
• 6. Coupon at bottom for "10th lawn service Free!"
Nice to have
• Art work from our website is fine to use, That carries our theme throughout our campaign.
Should not have
• Very wordy. This is basically a billboard, Have very few seconds to grab their attention.

```html
<!DOCTYPE html>
<html lang="en">
<head>
<meta charset="utf-8">
<title>VerdaTurf Door Hanger</title>
<link href="https://fonts.googleapis.com/css2?family=Montserrat:wght@700;800;900&family=Cinzel:wght@400;500&family=Oswald:wght@500;600&display=swap" rel="stylesheet">
<style>
:root{
  --stage:#2b2b2b;
  --paper:#ffffff;
  --ink:#0c0c0c;
  --red:#ea3a26;
  --grass-dark:#1f4a1c;
  --grass:#3f7f2a;
  --grass-light:#6aa83a;
  --white:#ffffff;
}
*{margin:0;padding:0;box-sizing:border-box}
html,body{width:982px;height:1200px;overflow:hidden;background:var(--stage)}
.canvas{position:relative;width:982px;height:1200px}
.hanger{position:absolute;top:50px;width:416px;height:1100px;background:var(--paper)}
.hanger--front{left:50px}
.hanger--back{left:518px}
.face{position:absolute;left:12px;top:12px;width:392px;height:1076px;overflow:hidden;background:var(--grass-dark)}
.abs{position:absolute}
.header{left:0;top:0;width:392px;height:68px;background:var(--ink);color:var(--white);
  font-family:'Montserrat',sans-serif;font-weight:800;font-size:37px;letter-spacing:1px;
  display:flex;align-items:center;justify-content:center;gap:14px;white-space:nowrap}
.photo{left:0;top:68px;width:392px;height:810px}
.photo--mower{background:linear-gradient(135deg,#4c8b2c 0%,#2e6a22 35%,#b52a1c 36%,#d23a22 55%,#3a6f25 56%,#1f4a1c 100%)}
.photo--family{height:330px;background:linear-gradient(180deg,#2e4a24 0%,#3d6a2c 55%,#5c9a36 100%)}
.grass-field{left:0;top:398px;width:392px;height:480px;background:linear-gradient(180deg,#4d8c2e,#2c5e21 60%,#1c3f18)}
.ribbon{left:0;top:68px}
.hole{width:128px;height:128px;border-radius:50%;background:var(--paper);left:130px;top:98px}
.panel{background:linear-gradient(180deg,#5a9834,#2a5a20);border:2px solid var(--white);color:var(--white);
  box-shadow:0 3px 8px rgba(0,0,0,.45)}
.panel--red{background:var(--red)}
.headline{font-family:'Montserrat',sans-serif;font-weight:900;text-shadow:2px 2px 3px rgba(0,0,0,.6);white-space:nowrap}
.serif{font-family:'Cinzel',serif;font-weight:500;white-space:nowrap}
.mowed{left:25px;top:250px;width:332px;height:268px;border-right:16px solid var(--red)}
.mowed p{position:absolute;left:28px;top:24px;font-size:35px;line-height:45px}
.mower-art{left:222px;top:197px;width:70px;height:46px;background:linear-gradient(90deg,#c42a1c,#ea3a26);border-radius:4px}
.area{left:25px;top:546px;width:332px;height:92px;text-align:center;font-size:31px;line-height:37px;padding-top:10px;text-shadow:1px 1px 2px rgba(0,0,0,.6)}
.day{left:25px;top:638px;width:332px;height:72px;text-align:center;font-size:38px;line-height:68px}
.call{left:25px;top:736px;width:332px;height:56px;text-align:center;font-size:28px;line-height:54px;text-shadow:1px 1px 2px rgba(0,0,0,.6)}
.call-phone{left:25px;top:792px;width:332px;height:58px;text-align:center;font-size:31px;line-height:56px}
.cut{left:0;top:878px;width:392px;border-top:2px dashed var(--white)}
.coupon-band{left:0;top:880px;width:392px;height:196px;background:linear-gradient(110deg,var(--red) 0%,var(--red) 60%,#e78a2a 85%,#a6c23a 100%)}
.coupon{left:16px;top:16px;width:360px;height:166px;background:linear-gradient(180deg,#1e4a1c,#2f6a26 50%,#173a16);border:2px solid var(--white);color:var(--white);overflow:hidden}
.coupon-line{left:0;top:18px;width:100%;text-align:center;font-family:'Cinzel',serif;font-size:29px;line-height:34px;white-space:nowrap}
.coupon-line sup{font-size:16px}
.free{left:22px;top:60px;font-family:'Oswald',sans-serif;font-weight:600;font-size:80px;line-height:90px;letter-spacing:-1px;white-space:nowrap}
.with{left:200px;top:70px;font-family:'Oswald',sans-serif;font-weight:600;font-size:30px;line-height:38px;letter-spacing:2px;white-space:nowrap}
.with span{display:block}
.with span + span{letter-spacing:7px}
.hardwork{left:36px;top:382px;width:318px;height:102px;border-left:14px solid var(--red);border-right:14px solid var(--red);font-size:31px;line-height:38px;padding:12px 0 0 32px}
.services{left:36px;top:518px;width:318px;height:232px;background:linear-gradient(180deg,#3c7a2a,#1a3a17)}
.services h2{height:40px;background:var(--red);text-align:center;font-family:'Montserrat',sans-serif;font-weight:800;font-size:21px;line-height:40px;letter-spacing:1px}
.services ul{list-style:none;padding:12px 0 0 22px}
.services li{display:flex;align-items:center;gap:10px;height:28.4px;font-family:'Cinzel',serif;font-size:18px;white-space:nowrap}
.tick{width:24px;height:24px;flex:none}
.contact{left:48px;top:768px;list-style:none;color:var(--white);font-family:'Montserrat',sans-serif;font-weight:700;font-size:15px}
.contact li{display:flex;align-items:center;gap:9px;height:31px;white-space:nowrap;text-shadow:1px 1px 2px rgba(0,0,0,.5)}
.contact svg{width:21px;height:21px;flex:none}
.back-name{left:0;top:26px;width:100%;text-align:center;font-family:'Montserrat',sans-serif;font-weight:800;font-size:44px;line-height:52px;white-space:nowrap}
.back-phone{left:0;top:82px;width:100%;text-align:center;font-family:'Oswald',sans-serif;font-weight:600;font-size:56px;line-height:64px;white-space:nowrap}
</style>
</head>
<body>
<div class="canvas">

  <section class="hanger hanger--front">
    <div class="face">
      <div class="abs photo photo--mower" role="img" aria-label="Close-up photo of a red lawn mower on fresh green grass"></div>
      <svg class="abs ribbon" width="220" height="220" viewBox="0 0 220 220" aria-hidden="true">
        <polygon points="0,104 104,0 166,0 0,166" fill="#ea3a26"/>
        <text transform="translate(64,62) rotate(-45)" fill="#fff" font-family="Montserrat,sans-serif" font-weight="800" font-size="15" text-anchor="middle">SERVICES</text>
        <text transform="translate(79,77) rotate(-45)" fill="#fff" font-family="Montserrat,sans-serif" font-weight="800" font-size="15" text-anchor="middle">GUARANTEED!</text>
      </svg>
      <div class="abs hole"></div>
      <header class="abs header">VERDATURF</header>

      <div class="abs panel mowed">
        <p class="headline">WE MOWED<br>YOUR<br>NEIGHBORS<br>LAWN<br>TODAY!</p>
        <div class="abs mower-art" role="img" aria-label="Small illustration of a red push mower"></div>
      </div>

      <div class="abs panel area serif">WE'RE IN THE<br>AREA EVERY</div>
      <div class="abs panel panel--red day headline">TUESDAY!</div>

      <div class="abs panel call serif">CALL US TODAY!</div>
      <div class="abs panel panel--red call-phone headline">512-748-3091</div>

      <div class="abs cut"></div>
      <div class="abs coupon-band">
        <div class="abs coupon">
          <div class="abs coupon-line">10<sup>TH</sup> LAWN SERVICE</div>
          <div class="abs free">FREE!</div>
          <div class="abs with"><span>WITH THIS</span><span>COUPON</span></div>
        </div>
      </div>
    </div>
  </section>

  <section class="hanger hanger--back">
    <div class="face">
      <div class="abs photo photo--family" role="img" aria-label="Photo of two children playing with balloons on a green lawn"></div>
      <div class="abs grass-field" role="img" aria-label="Photo of a lush green lawn"></div>
      <svg class="abs ribbon" width="220" height="220" viewBox="0 0 220 220" aria-hidden="true">
        <polygon points="0,104 104,0 166,0 0,166" fill="#ea3a26"/>
        <text transform="translate(64,62) rotate(-45)" fill="#fff" font-family="Montserrat,sans-serif" font-weight="800" font-size="15" text-anchor="middle">SERVICES</text>
        <text transform="translate(79,77) rotate(-45)" fill="#fff" font-family="Montserrat,sans-serif" font-weight="800" font-size="15" text-anchor="middle">GUARANTEED!</text>
      </svg>
      <div class="abs hole"></div>
      <header class="abs header">
        <svg width="32" height="32" viewBox="0 0 32 32" aria-hidden="true"><circle cx="16" cy="16" r="16" fill="#fff"/><path d="M11 8l3 0 1.5 5-2 1.5c1 2.3 2.7 4 5 5l1.5-2 5 1.5 0 3c0 1-1 2-2 2C14 24 8 18 8 10c0-1 1-2 3-2z" fill="#0c0c0c"/></svg>
        512-748-3091
      </header>

      <div class="abs panel hardwork headline">LET US DO THE<br>HARD WORK!</div>

      <div class="abs panel services">
        <h2>OUR SERVICES</h2>
        <ul>
          <li><svg class="tick" viewBox="0 0 24 24" aria-hidden="true"><circle cx="12" cy="12" r="11" fill="#ea3a26" stroke="#fff" stroke-width="1.5"/><path d="M7 12.5l3.2 3.2L17 9" fill="none" stroke="#fff" stroke-width="2.6"/></svg>LAWN MOWING</li>
          <li><svg class="tick" viewBox="0 0 24 24" aria-hidden="true"><circle cx="12" cy="12" r="11" fill="#ea3a26" stroke="#fff" stroke-width="1.5"/><path d="M7 12.5l3.2 3.2L17 9" fill="none" stroke="#fff" stroke-width="2.6"/></svg>FERTILIZATION</li>
          <li><svg class="tick" viewBox="0 0 24 24" aria-hidden="true"><circle cx="12" cy="12" r="11" fill="#ea3a26" stroke="#fff" stroke-width="1.5"/><path d="M7 12.5l3.2 3.2L17 9" fill="none" stroke="#fff" stroke-width="2.6"/></svg>WEED CONTROL</li>
          <li><svg class="tick" viewBox="0 0 24 24" aria-hidden="true"><circle cx="12" cy="12" r="11" fill="#ea3a26" stroke="#fff" stroke-width="1.5"/><path d="M7 12.5l3.2 3.2L17 9" fill="none" stroke="#fff" stroke-width="2.6"/></svg>LANDSCAPE SERVICES</li>
          <li><svg class="tick" viewBox="0 0 24 24" aria-hidden="true"><circle cx="12" cy="12" r="11" fill="#ea3a26" stroke="#fff" stroke-width="1.5"/><path d="M7 12.5l3.2 3.2L17 9" fill="none" stroke="#fff" stroke-width="2.6"/></svg>SPRINKLER REPAIR</li>
          <li><svg class="tick" viewBox="0 0 24 24" aria-hidden="true"><circle cx="12" cy="12" r="11" fill="#ea3a26" stroke="#fff" stroke-width="1.5"/><path d="M7 12.5l3.2 3.2L17 9" fill="none" stroke="#fff" stroke-width="2.6"/></svg>LANDSCAPE LIGHTING</li>
        </ul>
      </div>

      <ul class="abs contact">
        <li><svg viewBox="0 0 24 24" aria-hidden="true"><circle cx="12" cy="12" r="12" fill="#fff"/><path d="M8 6h2.3l1.1 3.7-1.5 1.1c.8 1.7 2 3 3.7 3.7l1.1-1.5 3.7 1.1V16.4c0 .8-.7 1.5-1.5 1.5C11 17.9 6.5 13.4 6.5 7.5 6.5 6.7 7.2 6 8 6z" fill="#1f4a1c"/></svg>512-748-3091</li>
        <li><svg viewBox="0 0 24 24" aria-hidden="true"><circle cx="12" cy="12" r="10.5" fill="none" stroke="#fff" stroke-width="1.8"/><ellipse cx="12" cy="12" rx="4.5" ry="10.5" fill="none" stroke="#fff" stroke-width="1.5"/><path d="M1.5 12h21M3.5 7h17M3.5 17h17" stroke="#fff" stroke-width="1.5"/></svg>WWW.VERDATURF-EXAMPLE.NET</li>
        <li><svg viewBox="0 0 24 24" aria-hidden="true"><circle cx="12" cy="12" r="12" fill="#fff"/><rect x="6" y="8" width="12" height="8.5" fill="none" stroke="#1f4a1c" stroke-width="1.6"/><path d="M6 8l6 5 6-5" fill="none" stroke="#1f4a1c" stroke-width="1.6"/></svg>HELLO@VERDATURF-EXAMPLE.NET</li>
      </ul>

      <div class="abs cut"></div>
      <div class="abs coupon-band">
        <div class="abs coupon">
          <div class="abs back-name">VERDATURF</div>
          <div class="abs back-phone">512-748-3091</div>
        </div>
      </div>
    </div>
  </section>

</div>
</body>
</html>
```